Dravel

We are openıng one huntıng showroom in Riyadh? Saudi Arabia. Company name is "DRAVEL".
Our logo designed and we need Business Card Design now.
I attached DRAVEL logo below.
Front side will English and back side will be Arabic

```html
<!DOCTYPE html>
<html lang="en">
<head>
<meta charset="utf-8">
<title>Dravel Business Cards</title>
<link href="https://fonts.googleapis.com/css2?family=Cairo:wght@400;700&family=Roboto:wght@400;700;900&display=swap" rel="stylesheet">
<style>
  :root {
    --bg: #2a2a2d;
    --green: #0c7c3f;
    --green-soft: #2f9a5c;
    --sage: #cdd8cc;
    --sage-deep: #b3c4b2;
    --olive: #789a1f;
    --white: #ffffff;
  }
  * { box-sizing: border-box; margin: 0; padding: 0; }
  html, body { width: 1200px; height: 800px; overflow: hidden; }
  body {
    background: var(--bg);
    font-family: "Roboto", Arial, sans-serif;
    position: relative;
  }
  .card {
    position: absolute;
    width: 540px;
    height: 310px;
    display: flex;
    overflow: hidden;
    box-shadow: 0 14px 30px rgba(0,0,0,.45);
  }
  .card--front { left: 80px; top: 70px; background: var(--green); }
  .card--back { left: 580px; top: 420px; background: var(--white); }

  .logo-panel {
    width: 170px;
    flex: none;
    display: flex;
    align-items: center;
    justify-content: center;
  }
  .card--front .logo-panel { background: var(--white); color: var(--green); }
  .card--back .logo-panel { background: var(--green); color: var(--white); }

  .brand {
    display: flex;
    align-items: center;
    gap: 12px;
    transform: rotate(90deg);
    white-space: nowrap;
  }
  .brand__name {
    font-family: "Roboto", Arial, sans-serif;
    font-weight: 900;
    font-size: 52px;
    letter-spacing: 1px;
    line-height: 1;
  }
  .brand__mark { width: 16px; height: 16px; background: currentColor; }

  .info-panel {
    flex: 1;
    position: relative;
    padding: 34px 0 0 34px;
  }
  .scene-art {
    position: absolute;
    right: 0; bottom: 0;
    width: 260px; height: 100%;
  }
  .card--front .scene-art {
    background: linear-gradient(90deg, rgba(47,154,92,0) 0%, rgba(47,154,92,.7) 50%, var(--green-soft) 100%);
  }
  .card--back .scene-art {
    background: linear-gradient(90deg, rgba(205,216,204,0) 0%, var(--sage) 55%, var(--sage-deep) 100%);
  }
  .content { position: relative; z-index: 1; width: 250px; }

  .person__name { font-weight: 700; font-size: 17px; letter-spacing: .3px; }
  .person__role { font-size: 13px; margin-top: 2px; }
  .card--front .content { color: var(--white); }
  .card--back .person__name { color: var(--green); }
  .card--back .person__role { color: var(--olive); }
  .card--back .contact-list { color: var(--green); }

  .contact-list { margin-top: 16px; font-size: 12.5px; }
  .contact-group {
    padding: 8px 0;
    border-bottom: 2px dotted currentColor;
  }
  .card--back .contact-group { border-bottom-color: var(--olive); }
  .contact-group:last-child { border-bottom: none; }
  .contact-row { display: flex; align-items: center; gap: 8px; line-height: 1.5; }
  .contact-row svg { width: 11px; height: 11px; flex: none; }
  .contact-row b { font-weight: 700; }
  .address { line-height: 1.4; }

  .content--arabic {
    font-family: "Cairo", Arial, sans-serif;
    text-align: right;
  }
  .content--arabic .person__name { font-size: 17px; letter-spacing: 0; }
  .content--arabic .contact-list { font-size: 12.5px; }
  .content--arabic .contact-row { line-height: 1.45; }
  .latin { direction: ltr; unicode-bidi: isolate; font-family: "Roboto", Arial, sans-serif; }
</style>
</head>
<body>

  <section class="card card--front">
    <div class="logo-panel">
      <div class="brand">
        <span class="brand__name">DRAVEL</span>
        <span class="brand__mark"></span>
      </div>
    </div>
    <div class="info-panel">
      <div class="scene-art" role="img" aria-label="Silhouette of a hunter aiming a rifle with a hunting dog and a flying pheasant in tall grass"></div>
      <div class="content">
        <p class="person__name">KARIM NASSER</p>
        <p class="person__role">Founder</p>
        <div class="contact-list">
          <div class="contact-group">
            <div class="contact-row"><svg viewBox="0 0 12 12"><rect x="1.5" y="1.5" width="9" height="9" fill="none" stroke="currentColor" stroke-width="1.4"/></svg><span>(555) 014-2287</span></div>
            <div class="contact-row"><svg viewBox="0 0 12 12"><rect x="1" y="4" width="10" height="7" fill="currentColor"/><rect x="3" y="1" width="6" height="3" fill="currentColor"/></svg><span>(555) 014-2287</span></div>
          </div>
          <div class="contact-group">
            <div class="contact-row"><svg viewBox="0 0 12 12"><rect x="0.5" y="2" width="11" height="8" fill="currentColor"/><path d="M1 2.5 6 7l5-4.5" fill="none" stroke="#0c7c3f" stroke-width="1"/></svg><span>info@dravelhunt.com</span></div>
            <div class="contact-row"><svg viewBox="0 0 12 12"><circle cx="6" cy="6" r="5.2" fill="none" stroke="currentColor" stroke-width="1.2"/><path d="M1 6h10M6 1c-2.5 3-2.5 7 0 10M6 1c2.5 3 2.5 7 0 10" fill="none" stroke="currentColor" stroke-width="1"/></svg><span>www.<b>dravelhunt</b>.com</span></div>
          </div>
          <div class="contact-group address">
            <p>PO BOX 88 Olaya Road</p>
            <p>King Fahd District Riyadh</p>
          </div>
        </div>
      </div>
    </div>
  </section>

  <section class="card card--back">
    <div class="logo-panel">
      <div class="brand">
        <span class="brand__name">DRAVEL</span>
        <span class="brand__mark"></span>
      </div>
    </div>
    <div class="info-panel">
      <div class="scene-art" role="img" aria-label="Pale silhouette of a hunter aiming a rifle with a hunting dog and a flying pheasant in tall grass"></div>
      <div class="content content--arabic" dir="rtl" lang="ar">
        <p class="person__name">كريم ناصر</p>
        <p class="person__role">المؤسس</p>
        <div class="contact-list">
          <div class="contact-group">
            <div class="contact-row"><svg viewBox="0 0 12 12"><rect x="1.5" y="1.5" width="9" height="9" fill="none" stroke="#789a1f" stroke-width="1.4"/></svg><span class="latin">(555) 014-2287</span></div>
            <div class="contact-row"><svg viewBox="0 0 12 12"><rect x="1" y="4" width="10" height="7" fill="#789a1f"/><rect x="3" y="1" width="6" height="3" fill="#789a1f"/></svg><span class="latin">(555) 014-2287</span></div>
          </div>
          <div class="contact-group">
            <div class="contact-row"><svg viewBox="0 0 12 12"><rect x="0.5" y="2" width="11" height="8" fill="#789a1f"/><path d="M1 2.5 6 7l5-4.5" fill="none" stroke="#fff" stroke-width="1"/></svg><span class="latin">info@dravelhunt.com</span></div>
            <div class="contact-row"><svg viewBox="0 0 12 12"><circle cx="6" cy="6" r="5.2" fill="none" stroke="#789a1f" stroke-width="1.2"/><path d="M1 6h10M6 1c-2.5 3-2.5 7 0 10M6 1c2.5 3 2.5 7 0 10" fill="none" stroke="#789a1f" stroke-width="1"/></svg><span class="latin">www.<b>dravelhunt</b>.com</span></div>
          </div>
          <div class="contact-group address">
            <p>ص.ب 88 طريق العليا</p>
            <p>حي الملك فهد، الرياض</p>
          </div>
        </div>
      </div>
    </div>
  </section>

</body>
</html>
```